Brand Voice Blueprint Book Cover Design

I'm about to publish the English version of my book on Brand Voice Blueprint. Name of the book is "Brand Voice Blueprint – How to untangle the online attention puzzle and leave your rivals behind". As a reference for colors and visual identity, I'm attaching the original book cover in Portuguese. I cannot reproduce the same cover due to my editor's copyright. I'm open to new fonts, font colors and illustrations that works well with the book title. I prefer a white or close to white solid or gradient background. I only need the front cover since the book will be published as an ebook format. The cover should show the title, subtitle, 3rd edition and my name "Tomas Veradello".

Target Market(s)

ebook publication on strategy / business

Industry/Entity Type

Business Management

Font styles to use
Sans Serif

Requirements
Must have
• The cover should show the title, subtitle, 3rd edition and my name "Tomas Veradello". White background. Should include a smart illustration that relates to the title. Illustration can be full of colors or more abstract. Use of shadows around the illustration is also ok. Keywords: social media, paradox, your company vs competitor, dialog, connection.
Nice to have
• Use the same visual identity from the first cover (attached).
Should not have
• Avoid the use of social media icons (from services like Chatterloom, Glimmerbox, etc.) or other kinds of icons such as phone, feed, wifi, etc.

```html
<!DOCTYPE html>
<html lang="en">
<head>
<meta charset="utf-8">
<title>Brand Voice Blueprint – Book Cover</title>
<link href="https://fonts.googleapis.com/css2?family=Montserrat:wght@400;500;600;800&display=swap" rel="stylesheet">
<style>
  :root {
    --paper: #ffffff;
    --title-green: #8cc63f;
    --title-navy: #23245e;
    --subtitle-orange: #e9531f;
    --network-purple: #4a2a86;
    --network-purple-soft: rgba(74, 42, 134, 0.22);
    --network-purple-fade: rgba(74, 42, 134, 0);
    --author-ink: #1c1c1c;
  }
  html, body {
    margin: 0;
    padding: 0;
    overflow: hidden;
    background: var(--paper);
  }
  .cover {
    position: relative;
    width: 750px;
    height: 1200px;
    background: var(--paper);
    overflow: hidden;
    font-family: "Montserrat", sans-serif;
  }
  .title {
    margin: 0;
    font-weight: 500;
  }
  .title-line {
    position: absolute;
    line-height: 1;
    white-space: nowrap;
    letter-spacing: -2px;
  }
  .title-line--first {
    left: 18px;
    top: 48px;
    font-size: 160px;
    color: var(--title-green);
  }
  .title-line--second {
    right: 78px;
    top: 196px;
    font-size: 160px;
    color: var(--title-green);
  }
  .title-line--third {
    left: 18px;
    top: 360px;
    font-size: 104px;
    font-weight: 800;
    color: var(--title-navy);
    letter-spacing: -1px;
  }
  .subtitle {
    position: absolute;
    left: 20px;
    top: 462px;
    margin: 0;
    font-size: 23px;
    line-height: 30px;
    font-weight: 400;
    color: var(--subtitle-orange);
  }
  .edition {
    position: absolute;
    left: 20px;
    top: 540px;
    margin: 0;
    font-size: 18px;
    font-weight: 600;
    letter-spacing: 3px;
    text-transform: uppercase;
    color: var(--title-navy);
  }
  .illustration {
    position: absolute;
    left: 270px;
    top: 545px;
    width: 450px;
    height: 490px;
    border-radius: 50%;
    background: radial-gradient(circle at 54% 47%, var(--network-purple-soft) 0%, var(--network-purple-fade) 70%);
  }
  .author {
    position: absolute;
    left: 18px;
    bottom: 80px;
    margin: 0;
    font-size: 44px;
    font-weight: 400;
    letter-spacing: 0.5px;
    color: var(--author-ink);
  }
</style>
</head>
<body>
  <main class="cover">
    <h1 class="title">
      <span class="title-line title-line--first">BRAND</span>
      <span class="title-line title-line--second">VOICE</span>
      <span class="title-line title-line--third">BLUEPRINT</span>
    </h1>
    <p class="subtitle">How to untangle the online attention puzzle<br>&amp; leave your rivals behind</p>
    <p class="edition">3rd edition</p>

    <div class="illustration" role="img" aria-label="Abstract illustration of a central hub linked to surrounding points, suggesting connection and dialogue between a company and its competitors"></div>

    <p class="author">TOMAS VERADELLO</p>
  </main>
</body>
</html>
```